Case Study - template Visual Design

We need to convert our current case study document into something more cosmetically pleasing and easy to read. (primary goal). We also want to make sure the design is reusable for future case studies as well.
Current case study content is uploaded for reference.
Company is Zentho.ai
Target Market(s)
Mid to large Enterprise
Industry/Entity Type
Iot
Font styles to use
Sans Serif
Colors
Designer to choose colors to be used in the design.

```html
<!DOCTYPE html>
<html lang="en">
<head>
<meta charset="utf-8">
<title>Zentho Case Study Template</title>
<link href="https://fonts.googleapis.com/css2?family=Roboto:wght@300;400;500;700;900&display=swap" rel="stylesheet">
<style>
  :root{
    --stage:#c8c8c8;
    --page-top:#f4f5f9;
    --page-bottom:#e3e4ea;
    --purple:#5a3ed8;
    --green:#4cbf82;
    --ink:#111111;
    --body:#6d6d74;
    --label:#1e1e1e;
  }
  *{box-sizing:border-box;margin:0;padding:0}
  html,body{width:1200px;height:656px;overflow:hidden;background:var(--stage);font-family:"Roboto",sans-serif}
  .stage{position:relative;width:1200px;height:656px}
  .page{position:absolute;top:79px;width:334px;height:473px;
    background:linear-gradient(160deg,var(--page-top),var(--page-bottom));
    box-shadow:0 2px 5px rgba(0,0,0,.18)}
  .page--front{left:69px}
  .page--inner{left:434px}
  .page--back{left:797px}
  .page-label{position:absolute;top:574px;width:334px;text-align:center;font-size:9.5px;font-weight:500;letter-spacing:1px;color:var(--label)}

  /* Front cover */
  .cover-mark{position:absolute;left:139px;top:42px;width:56px;height:56px;border-radius:10px;background:var(--purple)}
  .cover-name{position:absolute;left:0;right:0;top:124px;text-align:center;font-size:44px;font-weight:900;color:var(--ink);line-height:1}
  .cover-title{position:absolute;left:20px;right:20px;top:193px;text-align:center;color:var(--purple);font-size:17px;font-weight:700;line-height:18.2px;letter-spacing:.2px}
  .industry-grid{position:absolute;left:42px;top:274px;width:249px;display:grid;grid-template-columns:repeat(3,79px);gap:6px 6px}
  .industry-tile{height:79px;border-radius:11px}
  .industry-tile--purple{background:var(--purple)}
  .industry-tile--green{background:var(--green)}

  /* Inner page */
  .inner-brand{position:absolute;left:30px;top:36px;font-size:16px;font-weight:700;color:var(--ink)}
  .inner-content{position:absolute;left:30px;top:91px;width:273px}
  .inner-heading{font-size:10.9px;font-weight:700;line-height:13.6px;color:var(--ink);margin-bottom:4px}
  .inner-content p{font-size:8.5px;font-weight:300;line-height:11.2px;color:var(--body);text-align:justify;margin-bottom:11px}
  .inner-content strong{font-weight:400;color:var(--ink)}
  .inner-content .pull-quote{font-weight:400;color:var(--ink)}
  .page-rule{position:absolute;left:30px;top:436px;width:266px;height:1.5px;background:var(--purple)}
  .page-rule--end{left:298px;width:7px;background:var(--green)}
  .page-footer{position:absolute;top:442px;font-size:5px;font-weight:700;letter-spacing:.3px}
  .page-footer--site{left:30px;color:var(--purple)}
  .page-footer--num{right:30px;color:var(--green)}

  /* Back */
  .back-pattern{position:absolute;left:0;top:0;width:334px;height:341px;
    background:linear-gradient(180deg,#ebecf1 0%,#e6e7ed 70%,rgba(230,231,237,0) 100%)}
  .back-brand{position:absolute;left:0;right:0;top:301px;text-align:center;font-size:20px;font-weight:700;color:var(--ink)}
  .back-title{position:absolute;left:0;right:0;top:356px;text-align:center;font-size:14.5px;font-weight:700;color:var(--ink)}
  .back-about{position:absolute;left:57px;width:220px;top:383px;text-align:center;font-size:6.4px;line-height:9.5px;color:#333}
  .contact-bar{position:absolute;left:50%;transform:translateX(-50%);top:420px;height:17px;padding:0 5px;
    background:var(--purple);color:#fff;font-size:7.8px;font-weight:300;line-height:17px;text-align:center;white-space:nowrap}
  .contact-bar .sep{padding:0 3px}
  .copyright{position:absolute;left:0;right:0;top:447px;text-align:center;font-size:5.8px;color:#333}
</style>
</head>
<body>
<div class="stage">

  <section class="page page--front">
    <div class="cover-mark"></div>
    <div class="cover-name">Zentho</div>
    <h1 class="cover-title">HOW ZENTHO DRIVES ADOPTION<br>OF PREDICTIVE MAINTENANCE<br>WITH MACHINE LEARNING</h1>
    <div class="industry-grid">
      <div class="industry-tile industry-tile--purple" role="img" aria-label="Construction crane claw icon"></div>
      <div class="industry-tile industry-tile--green" role="img" aria-label="Manufacturing robot arm and containers icon"></div>
      <div class="industry-tile industry-tile--purple" role="img" aria-label="Industrial printing icon"></div>
      <div class="industry-tile industry-tile--green" role="img" aria-label="Oil and gas rig icon"></div>
      <div class="industry-tile industry-tile--purple" role="img" aria-label="Healthcare stethoscope icon"></div>
      <div class="industry-tile industry-tile--green" role="img" aria-label="Defense jet aircraft icon"></div>
    </div>
  </section>
  <div class="page-label" style="left:69px">FRONT</div>

  <section class="page page--inner">
    <div class="inner-brand">Zentho</div>
    <div class="inner-content">
      <h2 class="inner-heading">HOW ZENTHO DRIVES ADOPTION OF PREDICTIVE MAINTENANCE WITH MACHINE LEARNING</h2>
      <p>Predictive maintenance, or the practice of using data to anticipate equipment failures, has become a tool that delivers meaningful time and cost savings for a wide range of businesses. With an ability to reduce breakdowns by an average of <strong>70% and lower maintenance costs by an average of 25%,</strong> predictive maintenance is no longer an advanced R&amp;D initiative considered only by early adopters. It is delivering real results for assets used in manufacturing, construction, industrial printing, oil and gas exploration, healthcare, defense and more.</p>
      <p>At Zentho, we continue to develop machine learning tools that can bring predictive maintenance capabilities to businesses of all sizes dedicated to improving their operations, even those with modest budgets or</p>
      <p class="pull-quote">With an ability to reduce breakdowns by an average of 70% &amp; lower maintenance costs by an average of 25%, predictive maintenance is no longer an advanced R&amp;D initiative considered only by early adopters.</p>
      <p>limited technical capabilities. Our solutions have also helped department leaders be recognized for bringing a new and valuable analytics-based practice into the company.</p>
      <p>As the COVID-19 pandemic places new challenges on businesses of all types, those that adopt this valuable tool now will be better equipped to hit the ground running when global health and economic conditions improve.</p>
    </div>
    <div class="page-rule"></div>
    <div class="page-rule page-rule--end"></div>
    <div class="page-footer page-footer--site">ZENTHO.AI</div>
    <div class="page-footer page-footer--num">01</div>
  </section>
  <div class="page-label" style="left:434px">PAGE 1</div>

  <section class="page page--back">
    <div class="back-pattern" role="img" aria-label="Faint repeating brand pattern background"></div>
    <div class="back-brand">Zentho</div>
    <h2 class="back-title">CONTACT US</h2>
    <p class="back-about">We are a team of developers and data scientists from leading machine learning companies like Northwind, Altavia and Corebyte, working behind the scenes to deliver exceptional models and experiences.</p>
    <div class="contact-bar">+1 (555) 014-2290<span class="sep">|</span>hello@zentho.ai<span class="sep">|</span>www.zentho.ai</div>
    <p class="copyright">Copyright © 2020 • Ninefold Labs, Inc</p>
  </section>
  <div class="page-label" style="left:797px">BACK</div>

</div>
</body>
</html>
```